Exciting New Year's Eve Church Flyer for Watch Night Service

Need an eye catching, exciting New Year's Eve flyer for our church's watch night service. We are an exciting very energetic church. We like bold sharp colors. Must include verbiage but does not have to be in exact order.
Watch Night Service
If it had not been for the Lord
Meadow of Grace Community Church
482 Corvell St
New Braunfels Tx
December 31, 2018
10:30 pm till midnight

Target Market(s)

19-40 demographich

Requirements
Must have
• bold colors
Should not have
• Should not be serious nor too literal. A cross is not needed

```html
<!DOCTYPE html>
<html lang="en">
<head>
<meta charset="utf-8">
<title>Watch Night Service – Meadow of Grace Community Church</title>
<link rel="stylesheet" href="https://fonts.googleapis.com/css2?family=Alike&family=Great+Vibes&family=Cormorant+Garamond:ital,wght@1,500&display=swap">
<style>
  :root {
    --night-deep: #1c0827;
    --night-mid: #3a1450;
    --gold: #e2b25c;
    --ink-light: #ffffff;
    --skyline: #f5f5f7;
  }
  html, body {
    margin: 0;
    padding: 0;
    overflow: hidden;
    background: var(--night-deep);
  }
  .flyer {
    position: relative;
    width: 857px;
    height: 1200px;
    overflow: hidden;
    background: radial-gradient(ellipse at 50% 40%, var(--night-mid) 0%, #2a0d3b 45%, var(--night-deep) 100%);
    color: var(--ink-light);
    font-family: "Alike", Georgia, serif;
    text-align: center;
  }
  .church-name {
    position: absolute;
    top: 56px;
    left: 0;
    width: 100%;
    margin: 0;
    font-family: "Alike", Georgia, serif;
    font-weight: 400;
    font-size: 30px;
    line-height: 36px;
    letter-spacing: 3px;
    color: var(--gold);
    text-transform: uppercase;
  }
  .church-dot {
    display: block;
    width: 22px;
    height: 22px;
    margin: 0 auto 26px;
    border-radius: 50%;
    background: var(--gold);
  }
  .invite {
    position: absolute;
    top: 190px;
    left: 0;
    width: 100%;
    margin: 0;
    font-size: 31px;
    line-height: 48px;
    letter-spacing: 2px;
  }
  .title {
    position: absolute;
    top: 318px;
    left: 0;
    width: 100%;
    margin: 0;
    font-family: "Great Vibes", cursive;
    font-weight: 400;
    color: var(--gold);
    font-size: 138px;
    line-height: 128px;
    white-space: nowrap;
  }
  .title span { display: block; }
  .title .line-two { margin-left: 30px; }
  .tagline {
    position: absolute;
    top: 606px;
    left: 0;
    width: 100%;
    margin: 0;
    font-family: "Cormorant Garamond", Georgia, serif;
    font-style: italic;
    font-weight: 500;
    font-size: 34px;
    letter-spacing: 2px;
  }
  .details {
    position: absolute;
    top: 676px;
    left: 0;
    width: 100%;
    margin: 0;
    font-size: 23px;
    line-height: 33px;
    letter-spacing: 1.5px;
  }
  .details p { margin: 0 0 31px; }
  .skyline {
    position: absolute;
    left: 0;
    bottom: 0;
    width: 100%;
    height: 240px;
    background: linear-gradient(to bottom, rgba(245,245,247,0) 0%, rgba(245,245,247,0.6) 30%, var(--skyline) 55%);
  }
</style>
</head>
<body>
<main class="flyer">
  <h2 class="church-name"><span class="church-dot"></span>Meadow of Grace Community Church</h2>
  <p class="invite">Join us for a<br>night of merriment</p>
  <h1 class="title"><span class="line-one">Watch Night</span><span class="line-two">Service</span></h1>
  <p class="tagline">If it had not been the lord</p>
  <div class="details">
    <p>Where: Meadow of Grace Community<br>Church<br>482 Corvell St<br>New Braunfels Tx</p>
    <p>When: Monday, 31st of December</p>
    <p>Time: 10:30pm to Midnight</p>
  </div>
  <div class="skyline" role="img" aria-label="White silhouette of a town skyline of houses with small windows along the bottom edge"></div>
</main>
</body>
</html>
```